Label design for Cargo Pants.

We need modern packaging design for men's cargo pant for a brand name Vantu. All kinds of packaging designs are welcome.

The pant is folded and packaged in a poly bag. We require a label design for the brand name Vantu. The main label will be attached by a string on the belt loop. the size of that label will 25cm in length and 10cm wide. This is the first label the customer see's when he picks up the garment. Therefore, we require an eye catching design for that. If required it could have certain information about the chino pant on the main label such as Comfort fit, Wrinkle-resistant, machine washable, luxury fabric. But, if you feel that adding the above information spoils the design of the label then it is not a must to include the above information. On the back of the label we like to include the information that this pant was manufactured in an Quarv Platinum certified green plant and hence the damage to the environment because of the plant is nill.

The second label is attached on to the waist band and the purpose of that label is to include the size of the pant such 32x32. The size of that label is 8cm in length and 4cm in width. There is no design on the back on this label it has to be blank.

Sample, is provided for what we use for our chino pant.

```html
<!DOCTYPE html>
<html lang="en">
<head>
<meta charset="utf-8">
<title>Vantu Men's Chinos – Hang Tag and Waist Label</title>
<link rel="stylesheet" href="https://fonts.googleapis.com/css2?family=Montserrat:wght@500;600&family=Nunito+Sans:wght@600&family=Lora&display=swap">
<style>
  :root {
    --page: #ffffff;
    --tag: #87a9c0;
    --ink: #4a6f8c;
    --ink-soft: #5f84a1;
    --oval: #cfdee9;
    --light: #eef4f8;
  }
  html, body {
    margin: 0;
    width: 1200px;
    height: 1022px;
    overflow: hidden;
    background: var(--page);
  }
  .artboard { display: block; }
  .tag-fill { fill: var(--tag); }
  .ink-fill { fill: var(--ink); }
  .eyelet { fill: var(--ink); stroke: #ffffff; stroke-width: 6; }
  .oval-panel { fill: var(--oval); stroke: var(--ink); stroke-width: 4; }
  .wordmark {
    font-family: "Montserrat", sans-serif;
    font-weight: 600;
    fill: #ffffff;
    text-anchor: middle;
  }
  .subline {
    font-family: "Montserrat", sans-serif;
    font-weight: 500;
    fill: var(--ink);
    text-anchor: middle;
  }
  .feature-list {
    font-family: "Lora", serif;
    font-size: 17px;
    fill: var(--light);
    text-anchor: middle;
  }
  .eco-statement {
    font-family: "Nunito Sans", sans-serif;
    font-weight: 600;
    font-size: 19px;
    fill: #ffffff;
    text-anchor: middle;
  }
  .cta-text {
    font-family: "Nunito Sans", sans-serif;
    font-weight: 600;
    font-size: 18px;
    fill: var(--light);
    text-decoration: underline;
  }
  .rule { stroke: #c8d9e5; stroke-width: 1; }
  .badge-outline { fill: none; stroke: var(--ink); stroke-width: 2; }
</style>
</head>
<body>
<svg class="artboard" width="1200" height="1022" viewBox="0 0 1200 1022" xmlns="http://www.w3.org/2000/svg">
  <defs>
    <linearGradient id="illustration-tone" x1="0" y1="0" x2="1" y2="1">
      <stop offset="0" stop-color="#4a6f8c" stop-opacity="0.55"/>
      <stop offset="1" stop-color="#4a6f8c" stop-opacity="0.25"/>
    </linearGradient>
  </defs>

  <!-- Front of hang tag -->
  <g class="hang-tag-front">
    <rect class="tag-fill" x="45" y="52" width="382" height="953"/>
    <rect x="45" y="130" width="382" height="710" fill="url(#illustration-tone)" role="img" aria-label="Large engraved illustration of a moose with broad antlers"/>
    <circle class="eyelet" cx="236" cy="121" r="15"/>

    <ellipse class="oval-panel" cx="236" cy="565" rx="120" ry="225"/>
    <rect x="172" y="400" width="118" height="122" rx="6" fill="#8fadc3" role="img" aria-label="Small engraved illustration of a standing moose"/>

    <g class="brand-ribbon" transform="rotate(-8 236 590)">
      <polygon class="ink-fill" points="55,560 105,560 105,615 55,615 72,587"/>
      <polygon class="ink-fill" points="367,560 417,560 400,587 417,615 367,615"/>
      <rect class="ink-fill" x="105" y="540" width="262" height="95" stroke="var(--oval)" stroke-width="3"/>
      <text class="wordmark" x="236" y="615" font-size="72">VANTU</text>
      <text class="subline" x="236" y="658" font-size="19">MEN´S CHINOS</text>
      <line x1="166" y1="666" x2="306" y2="666" stroke="var(--ink)" stroke-width="2"/>
    </g>

    <circle class="badge-outline" cx="240" cy="742" r="36"/>

    <line class="rule" x1="55" y1="925" x2="417" y2="925"/>
    <text class="feature-list" x="236" y="956">Wrinkle resistant  |  Machine washable</text>
    <text class="feature-list" x="236" y="977">Luxury fabric</text>
  </g>

  <!-- Back of hang tag -->
  <g class="hang-tag-back">
    <rect class="tag-fill" x="446" y="52" width="381" height="953"/>
    <rect x="500" y="225" width="327" height="700" fill="url(#illustration-tone)" role="img" aria-label="Large engraved illustration of a moose head and body in profile"/>
    <circle class="eyelet" cx="636" cy="121" r="15"/>
    <circle cx="636" cy="215" r="66" fill="var(--ink-soft)" stroke="var(--ink)" stroke-width="3"/>

    <text class="eco-statement" x="636" y="523">THIS VANTU CHINO</text>
    <text class="eco-statement" x="636" y="584">WAS PROUDLY PRODUCED</text>
    <text class="eco-statement" x="636" y="645">IN A QUARV PLATINUM</text>
    <text class="eco-statement" x="636" y="706">CERTIFIED GREEN PLANT</text>
    <text class="eco-statement" x="636" y="767">WITH NO NEGATIVE</text>
    <text class="eco-statement" x="636" y="828">ENVIROMENTAL IMPACT</text>

    <rect class="ink-fill" x="585" y="899" width="182" height="48" rx="24"/>
    <circle cx="560" cy="918" r="56" fill="var(--ink)" stroke="var(--tag)" stroke-width="3"/>
    <text class="cta-text" x="625" y="931">BUY A VANTU !</text>
  </g>

  <!-- Waistband size label -->
  <g class="waist-label">
    <rect class="tag-fill" x="880" y="449" width="292" height="141"/>
    <rect x="996" y="458" width="56" height="58" rx="4" fill="#6f93ad" role="img" aria-label="Small engraved illustration of a standing moose"/>
    <g class="brand-ribbon" transform="rotate(-8 1026 548)">
      <polygon class="ink-fill" points="940,532 965,532 965,560 940,560 949,546"/>
      <polygon class="ink-fill" points="1087,532 1112,532 1103,546 1112,560 1087,560"/>
      <rect class="ink-fill" x="965" y="522" width="122" height="46" stroke="var(--tag)" stroke-width="2"/>
      <text class="wordmark" x="1026" y="557" font-size="33">VANTU</text>
      <text class="subline" x="1026" y="581" font-size="10">MEN´S CHINOS</text>
    </g>
  </g>
</svg>
</body>
</html>
```